Modern Business Card

Modern professional business card with more than just logo and demographic info. Something memorable.

We are a trendy/modern chiropractic group with an emphasis on neurology, hence the minimalist-type brain logo. We want to convey that modern and technical aspect with professionalism and the elite nature of our practice environment.

```html
<!DOCTYPE html>
<html lang="en">
<head>
<meta charset="utf-8">
<title>Keystone Chiropractic – Business Card</title>
<link href="https://fonts.googleapis.com/css2?family=Libre+Baskerville&family=Montserrat:wght@400;500&display=swap" rel="stylesheet">
<style>
  :root {
    --brand-blue: #4a80c2;
    --brand-tint: #e9eff8;
    --ink: #1f1f22;
    --muted: #444a55;
    --paper: #ffffff;
    --backdrop: #e4e4e4;
    --serif: "Libre Baskerville", Georgia, serif;
    --sans: "Montserrat", Arial, sans-serif;
  }
  * { box-sizing: border-box; margin: 0; padding: 0; }
  html, body { width: 1200px; height: 930px; overflow: hidden; }
  body {
    background: var(--backdrop);
    display: flex;
    align-items: center;
    justify-content: center;
    gap: 40px;
  }
  .card {
    position: relative;
    width: 540px;
    height: 310px;
    border-radius: 22px;
    overflow: hidden;
    box-shadow: 0 6px 16px rgba(0,0,0,0.18);
  }

  /* Shared wordmark */
  .wordmark {
    display: flex;
    align-items: center;
    gap: 14px;
    font-family: var(--serif);
    font-weight: 400;
    text-transform: uppercase;
  }
  .wordmark__dot { border-radius: 50%; flex: none; }
  .wordmark__name { line-height: 1.05; }

  /* Front */
  .card--front {
    background: var(--brand-blue);
    display: flex;
    align-items: center;
    justify-content: center;
  }
  .card--front .wordmark { color: var(--paper); font-size: 30px; }
  .card--front .wordmark__dot { background: var(--paper); width: 56px; height: 56px; }

  /* Back */
  .card--back { background: var(--paper); }
  .card--back .wordmark {
    position: absolute;
    top: 36px; right: 32px;
    color: var(--ink);
    font-size: 19px;
    z-index: 2;
  }
  .card--back .wordmark__dot { background: var(--brand-blue); width: 32px; height: 32px; }

  .brand-motif {
    position: absolute;
    left: 190px; top: 92px;
    width: 240px; height: 150px;
    border-radius: 75px;
    background: linear-gradient(135deg, var(--brand-tint), #dfe8f4);
    z-index: 0;
  }

  .holder {
    position: absolute;
    top: 106px; left: 0;
    padding-left: 40px;
    z-index: 2;
  }
  .holder__accent {
    position: absolute;
    left: 0; top: 6px;
    width: 14px; height: 46px;
    background: var(--brand-blue);
  }
  .holder__name {
    font-family: var(--serif);
    color: var(--brand-blue);
    font-size: 17px;
    letter-spacing: 0.3px;
    text-transform: uppercase;
  }
  .holder__role {
    font-family: var(--sans);
    color: var(--muted);
    font-size: 13px;
    margin-top: 4px;
    padding-left: 14px;
  }

  .info-band {
    position: absolute;
    left: 0; right: 0; bottom: 0;
    height: 130px;
    background: var(--brand-blue);
    color: var(--paper);
    font-family: var(--sans);
    font-size: 13px;
    z-index: 1;
  }
  .contact {
    position: absolute;
    left: 44px; bottom: 20px;
    list-style: none;
  }
  .contact li {
    display: flex;
    align-items: center;
    gap: 10px;
    line-height: 22px;
  }
  .contact svg { width: 12px; height: 12px; flex: none; }
  .address {
    position: absolute;
    right: 32px; top: 28px;
    text-align: right;
    font-style: normal;
    line-height: 21px;
  }
</style>
</head>
<body>

  <section class="card card--front" aria-label="Card front">
    <div class="wordmark">
      <span class="wordmark__dot"></span>
      <span class="wordmark__name">Keystone<br>Chiropractic</span>
    </div>
  </section>

  <section class="card card--back" aria-label="Card back">
    <div class="brand-motif" role="img" aria-label="Large faint brand decoration in pale blue"></div>

    <div class="wordmark">
      <span class="wordmark__dot"></span>
      <span class="wordmark__name">Keystone<br>Chiropractic</span>
    </div>

    <div class="holder">
      <span class="holder__accent"></span>
      <p class="holder__name">Martin Hale</p>
      <p class="holder__role">Director</p>
    </div>

    <div class="info-band">
      <ul class="contact">
        <li>
          <svg viewBox="0 0 24 24" fill="currentColor" aria-hidden="true"><path d="M6.6 10.8a15 15 0 0 0 6.6 6.6l2.2-2.2a1 1 0 0 1 1-.25 11.4 11.4 0 0 0 3.6.57 1 1 0 0 1 1 1V20a1 1 0 0 1-1 1A17 17 0 0 1 3 4a1 1 0 0 1 1-1h3.5a1 1 0 0 1 1 1c0 1.25.2 2.45.57 3.57a1 1 0 0 1-.25 1z"/></svg>
          (555) 014-2290
        </li>
        <li>
          <svg viewBox="0 0 24 24" fill="none" stroke="currentColor" stroke-width="2" aria-hidden="true"><rect x="3" y="5" width="18" height="14" rx="1"/><path d="M3 6l9 7 9-7"/></svg>
          info@keystonechiro.com
        </li>
        <li>
          <svg viewBox="0 0 24 24" fill="none" stroke="currentColor" stroke-width="2" aria-hidden="true"><circle cx="12" cy="12" r="9"/><path d="M3 12h18M12 3c3 3.5 3 14.5 0 18M12 3c-3 3.5-3 14.5 0 18"/></svg>
          www.keystonechiro.com
        </li>
      </ul>
      <address class="address">418 Cedar Bend<br>Salem, OR 97301</address>
    </div>
  </section>

</body>
</html>
```